The Wellness Barn Business Card

Info for the front..... (in whichever order and layout looks best)
Carla Penhallow
Physiotherapist
4/37 Upper Creekbank Rd
Tallowbrook
QLD 4712
0462305178
carlapenhallow57@mailbox.example
www.thewellnessbarn.example.au
on the back I would like to be able to write appointments so probably just that heading with lines.
I like a sort of rustic style but mostly professional, colours in naturals, beige, brown, green etc. I dont mind if the logo colour is changed slightly to suit.

```html
<!DOCTYPE html>
<html lang="en">
<head>
<meta charset="UTF-8">
<title>The Wellness Barn – Business Card</title>
<link href="https://fonts.googleapis.com/css2?family=Lato:wght@400;700;900&display=swap" rel="stylesheet">
<style>
  :root {
    --green: #2d4a1f;
    --ink: #1e1e1e;
    --card: #ffffff;
    --backdrop: #3a3a3a;
    --rule: #2a2a2a;
  }
  * { box-sizing: border-box; margin: 0; padding: 0; }
  html, body { width: 1200px; height: 689px; overflow: hidden; }
  body {
    background: var(--backdrop);
    font-family: "Lato", sans-serif;
    display: flex;
    align-items: center;
    justify-content: center;
    gap: 40px;
  }
  .card {
    width: 540px;
    height: 309px;
    background: var(--card);
    border-radius: 20px;
    overflow: hidden;
    position: relative;
  }

  /* Back: appointments */
  .appointments-band {
    height: 112px;
    background: var(--green);
    display: flex;
    align-items: center;
    justify-content: center;
  }
  .appointments-title {
    color: #fff;
    font-weight: 700;
    font-size: 44px;
    letter-spacing: 2px;
  }
  .appointment-lines {
    list-style: none;
    padding: 24px 50px 0;
  }
  .appointment-lines li {
    height: 40px;
    border-bottom: 1px solid var(--rule);
  }

  /* Front: details */
  .front {
    display: flex;
    align-items: center;
    padding: 0 34px 0 30px;
  }
  .brand {
    width: 215px;
    display: flex;
    align-items: center;
    justify-content: center;
    color: var(--green);
    font-weight: 900;
    font-size: 34px;
    line-height: 1.05;
    text-align: center;
  }
  .divider {
    width: 1px;
    height: 190px;
    background: var(--green);
    margin: 0 22px 0 14px;
  }
  .details { color: var(--ink); font-size: 12.5px; line-height: 1.45; }
  .name { color: var(--green); font-weight: 700; font-size: 20px; line-height: 1.2; }
  .role { font-size: 13px; margin-bottom: 14px; }
  .contact { list-style: none; margin-bottom: 14px; }
  .contact li { display: flex; align-items: center; gap: 8px; }
  .contact svg { width: 12px; height: 12px; flex: none; fill: var(--green); }
  .address { font-style: normal; font-size: 13px; }
</style>
</head>
<body>

  <section class="card back">
    <div class="appointments-band">
      <h2 class="appointments-title">APPOINTMENTS</h2>
    </div>
    <ul class="appointment-lines">
      <li></li><li></li><li></li><li></li>
    </ul>
  </section>

  <section class="card front">
    <div class="brand">The<br>Wellness<br>Barn</div>
    <div class="divider"></div>
    <div class="details">
      <h1 class="name">Carla Penhallow</h1>
      <p class="role">Physiotherapist</p>
      <ul class="contact">
        <li>
          <svg viewBox="0 0 24 24" aria-hidden="true"><path d="M6.6 10.8a15.1 15.1 0 0 0 6.6 6.6l2.2-2.2c.3-.3.7-.4 1-.2 1.1.4 2.3.6 3.6.6.6 0 1 .4 1 1V20c0 .6-.4 1-1 1A17 17 0 0 1 3 4c0-.6.4-1 1-1h3.5c.6 0 1 .4 1 1 0 1.3.2 2.5.6 3.6.1.3 0 .7-.2 1z"/></svg>
          0462305178
        </li>
        <li>
          <svg viewBox="0 0 24 24" aria-hidden="true"><path d="M2 5h20v14H2z M2 5l10 8 10-8" fill="var(--green)"/><path d="M3 6l9 7 9-7" stroke="#fff" stroke-width="1.6" fill="none"/></svg>
          carlapenhallow57@mailbox.example
        </li>
        <li>
          <svg viewBox="0 0 24 24" aria-hidden="true"><circle cx="12" cy="12" r="10"/><path d="M2 12h20M12 2c3 3 3 17 0 20M12 2c-3 3-3 17 0 20" stroke="#fff" stroke-width="1.4" fill="none"/></svg>
          www.thewellnessbarn.example.au
        </li>
      </ul>
      <address class="address">4/37 Upper Creekbank Rd<br>Tallowbrook QLD 4712</address>
    </div>
  </section>

</body>
</html>
```